Business Card & Word Docs from existing Logo

We need a business card with typical information plus layout to include electrical contractors license number, VONEL license and KMP license. We would like a word document layout for a proposal document, opening page with logo and design basic information; proposal to and proposal from and project name and number. Small basic single page letter for general documents. Email signature with logo.

We are an electrical, refrigeration and automation contractor. We work with reducing energy consumption for our customers and complex process solutions in electrical, refrigeration and automation.

Reason: Final changes/ revisions to designs.

Target Market(s)

Industrial and commercial businesses that require more than your average contractor.

Industry/Entity Type

Electrical

Requirements
Must have
• Propsal document must have a full opening page.

```html
<!DOCTYPE html>
<html lang="en">
<head>
<meta charset="utf-8">
<title>Northvale Contracting – Proposal Cover</title>
<link rel="stylesheet" href="https://fonts.googleapis.com/css2?family=Open+Sans:wght@600&family=Arimo:wght@400;700&family=Didact+Gothic&display=swap">
<style>
  :root {
    --paper: #ffffff;
    --brand-blue: #1778ad;
    --brand-mark: #1c8fa8;
    --ink: #111111;
    --navy: #0d2a5c;
    --muted-ink: #333333;
    --band-start: #4a98ec;
    --band-mid: #2bb3a6;
    --band-end: #00e23c;
  }
  * { margin: 0; padding: 0; box-sizing: border-box; }
  html, body {
    width: 927px;
    height: 1200px;
    overflow: hidden;
    background: var(--paper);
  }
  .cover-page {
    position: relative;
    width: 927px;
    height: 1200px;
    background: var(--paper);
  }
  .brand-lockup {
    position: absolute;
    left: 182px;
    top: 268px;
    display: flex;
    align-items: center;
    gap: 22px;
  }
  .brand-dot {
    width: 104px;
    height: 104px;
    border-radius: 50%;
    background: var(--brand-mark);
    flex: none;
  }
  .brand-name {
    font-family: "Open Sans", sans-serif;
    font-weight: 600;
    font-size: 40px;
    line-height: 1.15;
    letter-spacing: 1px;
    color: var(--brand-blue);
  }
  .license-line {
    position: absolute;
    left: 0;
    width: 912px;
    top: 434px;
    text-align: center;
    font-family: "Arimo", sans-serif;
    font-size: 14px;
    color: var(--ink);
  }
  .proposal-from {
    position: absolute;
    left: 538px;
    top: 960px;
    font-family: "Arimo", sans-serif;
    font-weight: 700;
    font-size: 21px;
    color: var(--navy);
  }
  .proposal-date {
    position: absolute;
    left: 633px;
    top: 1015px;
    font-family: "Didact Gothic", sans-serif;
    font-size: 18px;
    letter-spacing: 0.5px;
    color: var(--muted-ink);
  }
  .footer-band {
    position: absolute;
    left: 57px;
    top: 1066px;
    width: 870px;
    height: 23px;
    background: linear-gradient(90deg, var(--band-start) 0%, var(--band-mid) 50%, var(--band-end) 100%);
  }
</style>
</head>
<body>
  <main class="cover-page">
    <div class="brand-lockup">
      <span class="brand-dot"></span>
      <span class="brand-name">NORTHVALE<br>CONTRACTING</span>
    </div>
    <p class="license-line">Electrical Contractors License 12345,&nbsp; KMP1234567,&nbsp; VONEL AA12345</p>
    <p class="proposal-from">Proposal from Mark Dalton</p>
    <p class="proposal-date">Date:</p>
    <div class="footer-band"></div>
  </main>
</body>
</html>
```